Like us

We need a contest ad that offers a free weekend getaway stay in our Spa Suite- Bridal or Family Suite or King Suite, winners choice. (subject to availability, some conditions apply)
Objective - to encourage existing followers to refer friends and obtain new likes. Each referral "like" should leave a comment with just the referral name in the comment line. We will compile these referral names and the new like names for 1 "referer" weekend getaway package & 1 new "like" weekend getaway package Prize package includes a dinner certificate at the Vorlan Grill (value $ 30) & a complimentary bottle of champagne
(In room or at the Restaurant.) Plimbook Contest closes June 30th, 2014. The professional image is the important part of the design, comment lines can be used for contest explanations, however it would be nice to incorporate in the design. Design first!
The Motel Logo is AR Bonnie with a shadow. (bad copy uploaded)

Target Market(s)

Travelers

Industry/Entity Type

Restaurant

Requirements
Must have
• Professional Image
Nice to have
• Explanation of contest

```html
<!DOCTYPE html>
<html lang="en">
<head>
<meta charset="utf-8">
<title>Weekend Getaway Contest</title>
<link rel="stylesheet" href="https://fonts.googleapis.com/css2?family=Oswald:wght@500;700&family=Open+Sans:wght@400;600;700;800&display=swap">
<style>
  :root {
    --red: #d0202a;
    --blue: #2b6cc4;
    --like-blue: #4a6bb0;
    --gold: #f5c518;
    --white: #ffffff;
    --ink: #2a2a2a;
    --muted: #555555;
    --panel: rgba(20, 20, 24, 0.74);
    --room-dark: #2b1a12;
    --room-mid: #7a5235;
    --room-warm: #c89a62;
  }
  * { margin: 0; padding: 0; box-sizing: border-box; }
  html, body { width: 880px; height: 1200px; overflow: hidden; background: var(--white); }
  .poster {
    position: relative;
    width: 880px;
    height: 1200px;
    background: var(--white);
    font-family: "Open Sans", Arial, sans-serif;
    color: var(--ink);
  }
  .headline {
    position: absolute;
    left: 0;
    top: 14px;
    width: 560px;
    text-align: center;
  }
  .headline__title {
    font-family: "Oswald", Impact, sans-serif;
    font-weight: 700;
    font-size: 62px;
    letter-spacing: 18px;
    color: var(--red);
    line-height: 1;
  }
  .headline__deadline {
    margin-top: 10px;
    font-size: 27px;
    font-weight: 600;
    color: var(--blue);
  }
  .like-button {
    position: absolute;
    left: 690px;
    top: 42px;
    width: 140px;
    height: 54px;
    border-radius: 8px;
    background: var(--like-blue);
    border: 2px solid #c9d3e8;
    color: var(--white);
    font-weight: 700;
    font-size: 26px;
    line-height: 50px;
    text-align: center;
  }
  .cursor {
    position: absolute;
    left: 790px;
    top: 60px;
  }
  .hero-photo {
    position: absolute;
    left: 0;
    top: 175px;
    width: 880px;
    height: 835px;
    background:
      radial-gradient(ellipse at 18% 25%, rgba(255, 214, 140, 0.75), transparent 35%),
      radial-gradient(ellipse at 20% 82%, rgba(220, 200, 150, 0.55), transparent 30%),
      linear-gradient(160deg, var(--room-warm) 0%, var(--room-mid) 40%, var(--room-dark) 100%);
  }
  .offer-panel {
    position: absolute;
    left: 350px;
    top: 262px;
    width: 505px;
    height: 730px;
    border-radius: 16px;
    background: var(--panel);
    color: var(--white);
    padding: 18px 30px 24px;
  }
  .offer-panel__win {
    font-family: "Oswald", Impact, sans-serif;
    font-weight: 700;
    font-size: 108px;
    line-height: 1;
    text-align: center;
    letter-spacing: 4px;
  }
  .offer-panel__getaway {
    text-align: center;
    font-size: 30px;
    font-weight: 600;
    margin-top: 4px;
  }
  .offer-panel__suites {
    text-align: center;
    font-size: 25px;
    font-weight: 600;
    margin-top: 16px;
  }
  .offer-panel__choice {
    text-align: center;
    font-size: 36px;
    font-weight: 800;
    color: var(--gold);
    margin-top: 6px;
  }
  .offer-panel__heading {
    font-size: 22px;
    font-weight: 800;
    color: var(--gold);
    margin-top: 18px;
  }
  .steps {
    list-style: none;
    font-size: 19px;
    line-height: 1.3;
    margin-top: 2px;
  }
  .steps b { font-weight: 800; }
  .prize-text {
    font-size: 19px;
    line-height: 1.3;
    margin-top: 2px;
  }
  .conditions {
    position: absolute;
    left: 420px;
    top: 1025px;
    font-size: 18px;
    color: var(--ink);
  }
  .brand {
    position: absolute;
    text-align: center;
    color: var(--ink);
  }
  .brand--motel { left: 410px; top: 1085px; width: 240px; }
  .brand--grill { left: 690px; top: 1070px; width: 170px; }
  .brand__name {
    font-size: 30px;
    font-weight: 800;
    line-height: 1.05;
  }
  .brand__tagline {
    font-size: 12px;
    margin-top: 4px;
    color: var(--muted);
  }
</style>
</head>
<body>
<main class="poster">
  <header class="headline">
    <h1 class="headline__title">CONTEST</h1>
    <p class="headline__deadline">Contest closes June 30th, 2014.</p>
  </header>

  <div class="like-button">Like</div>
  <svg class="cursor" width="48" height="56" viewBox="0 0 48 56" aria-hidden="true">
    <path d="M14 4 v26 l-6 -5 c-3 -2 -6 1 -4 4 l12 18 h22 l4 -14 v-10 c0 -3 -4 -3 -4 0 v-2 c0 -3 -4 -3 -4 0 v-2 c0 -3 -4 -3 -4 0 v-15 c0 -4 -6 -4 -6 0 z" fill="#fff" stroke="#222" stroke-width="2.5" stroke-linejoin="round"/>
  </svg>

  <div class="hero-photo" role="img" aria-label="Warmly lit motel suite with bed and lamp, and two champagne flutes beside a bottle of sparkling wine in the foreground"></div>

  <section class="offer-panel">
    <div class="offer-panel__win">WIN</div>
    <p class="offer-panel__getaway">A WEEKEND GETAWAY!</p>
    <p class="offer-panel__suites">Spa, Family or King Suite</p>
    <p class="offer-panel__choice">WINNERS CHOICE!</p>

    <h2 class="offer-panel__heading">How to Participate</h2>
    <ol class="steps">
      <li><b>1.</b> Refer a friend to our Plimbook page</li>
      <li><b>2.</b> Have your friend "LIKE" our page and leave a comment with your name.</li>
      <li><b>3.</b> That's it! You and your friend are entered for a chance to win a weekend getaway package . (one for you, the referrer and one package for the friend you referred.)</li>
    </ol>

    <h2 class="offer-panel__heading">Getaway Prize Package includes:</h2>
    <p class="prize-text">A 2 night stay in our Spa, Family or King Suite, winners choice. A dinner certificate from the Vorlan Grill ($ 30 value) and a complimentary bottle of wine.</p>
  </section>

  <p class="conditions">*conditions apply</p>

  <div class="brand brand--motel">
    <p class="brand__name">HARLOW'S MOTEL</p>
    <p class="brand__tagline">Comfort Close to Home</p>
  </div>

  <div class="brand brand--grill">
    <p class="brand__name">Vorlan<br>Grill</p>
    <p class="brand__tagline">Fine Dining Lounge</p>
  </div>
</main>
</body>
</html>
```